Law Firm Specializing In Long-Term Care Negligence Needs a New Website

We have been using the same website for about 10 years. We need a new, fresh website design that will help us attract new clients. Many of our clients find us through Google search and the website is the first contact with the firm. Our current website is www.tarvelinlaw.com. We want to continue to have good placement on Google search using the terms that are currently used in the website. We have been on Google search for a long time and have good SEO placement without spending money on SEO optimization. Need to stand out from the competition. We are the only law firm in North Carolina that only handles cases involving long-term care negligence.

Target Market(s)

Individuals searching for an attorney who specializes in cases involving long-term care negligence. Cases against nursing homes, assisted living facilities, group homes.

Industry/Entity Type

Law Firm

Logo Text

Tarvelin Law

Coding

Coded - Design and coding required

Number of Pages Required

5+ page

Requirements
Must have
• I would like to have the same pages that I currently have on my website. I am trying to freshen up the website.

```html
<!DOCTYPE html>
<html lang="en">
<head>
<meta charset="utf-8">
<title>Tarvelin Law</title>
<link href="https://fonts.googleapis.com/css2?family=Lato:wght@400;700;900&family=Oswald:wght@400;500&display=swap" rel="stylesheet">
<style>
:root{
  --olive:#7b7650;
  --olive-dark:#5f5b3c;
  --ink:#222;
  --dark:#1c1c1c;
  --muted:#777;
  --paper:#fff;
  --page:#efefef;
  --line:#d8d8d8;
}
*{margin:0;padding:0;box-sizing:border-box}
html,body{width:845px;height:1200px;overflow:hidden}
body{background:var(--page);font-family:'Lato',sans-serif;color:var(--ink);font-size:7px;line-height:1.5}
.site{position:absolute;left:152px;top:0;width:541px;height:1200px;background:var(--paper)}
.topbar{height:28px;display:flex;align-items:center;justify-content:space-between;padding:0 10px}
.brand{font-family:'Lato',sans-serif;font-weight:700;font-size:13px;color:var(--ink)}
.search{width:70px;height:11px;border:1px solid var(--line)}
.nav{height:22px;background:var(--olive);display:flex;align-items:center;justify-content:space-around;padding:0 10px}
.nav a{color:#fff;text-decoration:none;font-size:5.5px;font-weight:700;letter-spacing:.4px;text-transform:uppercase}
.nav a.active{background:#fff;color:var(--olive);padding:2px 5px}
.hero{position:relative;height:275px;background:linear-gradient(90deg,#2b2a24 0%,#3d3a30 45%,#6e6450 80%,#8b7c60 100%);color:#fff}
.hero-copy{position:absolute;left:16px;top:48px;width:240px}
.hero h1{font-family:'Oswald',sans-serif;font-weight:400;font-size:19px;letter-spacing:.5px;margin-bottom:8px}
.hero p{font-size:6px;line-height:1.6;margin-bottom:14px}
.btn{display:inline-block;font-size:6.5px;font-weight:700;letter-spacing:.6px;text-transform:uppercase;padding:7px 14px}
.btn-light{background:#fff;color:var(--ink)}
.btn-olive{background:var(--olive);color:#fff}
.welcome{text-align:center;padding:24px 30px 20px}
.welcome h2{font-family:'Oswald',sans-serif;font-weight:400;font-size:18px;color:var(--olive);margin-bottom:8px}
.welcome p{font-size:5.5px;color:var(--muted);margin-bottom:12px;text-align:left}
.practice{margin:4px 15px 0;height:290px;background:linear-gradient(180deg,#1a1a1a,#262626);color:#fff;text-align:center;padding:26px 30px}
.practice h2{font-family:'Oswald',sans-serif;font-weight:400;font-size:18px;color:var(--olive);margin-bottom:8px}
.practice > p{font-size:5.5px;margin-bottom:16px}
.cards{display:flex;gap:16px;justify-content:center}
.card{width:118px;height:150px;background:var(--olive-dark);padding:16px 10px}
.card .icon{width:32px;height:32px;margin:0 auto 14px;display:block}
.card h3{font-size:6px;font-weight:700;text-transform:uppercase;margin-bottom:6px}
.card p{font-size:5px;margin-bottom:8px}
.card .more{display:inline-block;background:var(--dark);font-size:4.5px;padding:3px 6px;text-transform:uppercase}
.contact{display:flex;gap:22px;padding:18px 15px 0;height:240px}
.team{width:240px}
.team-photo{height:160px;background:linear-gradient(135deg,#8aa0b4,#d7d9db 55%,#6c7c8c)}
.team p{font-size:5px;color:var(--muted);margin-top:5px}
.ask{flex:1}
.ask h2{font-family:'Oswald',sans-serif;font-weight:400;font-size:14px;color:var(--olive);margin-bottom:8px}
.field{display:flex;align-items:center;border:1px solid var(--line);height:16px;margin-bottom:6px;padding:0 6px;font-size:5px;color:#999}
.field.message{height:42px;align-items:flex-start;padding-top:4px}
.ask .btn{padding:6px 14px}
.footer{position:absolute;left:0;top:1040px;width:541px;height:130px;background:var(--dark);color:#ccc;display:flex;gap:18px;padding:18px 15px}
.footer h4{font-size:6px;color:#fff;font-weight:700;text-transform:uppercase;margin-bottom:6px}
.footer ul{list-style:none}
.footer li{font-size:5px;line-height:2}
.col{flex:1}
.follow{margin-top:8px}
.socials{display:flex;gap:5px;margin-top:4px}
.socials span{width:10px;height:10px;border-radius:50%;background:#888}
.news input{display:block;width:100%;height:11px;border:0;background:#444;margin-bottom:5px}
.news .btn{padding:3px 8px;font-size:5px;background:#fff;color:var(--ink)}
.copyright{position:absolute;left:0;top:1170px;width:541px;height:30px;background:var(--olive);color:#fff;font-size:5px;display:flex;align-items:center;justify-content:center}
</style>
</head>
<body>
<div class="site">
  <header class="topbar">
    <div class="brand">Tarvelin Law</div>
    <div class="search"></div>
  </header>
  <nav class="nav">
    <a class="active">Home</a><a>About Tarvelin Law Project</a><a>Results</a><a>Our Team</a><a>Resources</a><a>Blog</a><a>Contact Us</a>
  </nav>

  <section class="hero" role="img" aria-label="Lawyer at a desk with scales of justice and a gavel">
    <div class="hero-copy">
      <h1>LOREM IPSUM DUMMY</h1>
      <p>Lorem ipsum dolor sit amet, consectetur adipiscing elit. Sed do eiusmod tempor incididunt ut labore et dolore magna aliqua. Ut enim ad minim veniam, quis nostrud exercitation ullamco.</p>
      <span class="btn btn-light">Read More</span>
    </div>
  </section>

  <section class="welcome">
    <h2>WELCOME TO OUR FIRM</h2>
    <p>Tarvelin Law is one of the only firms in North Carolina that handles only cases involving long-term care negligence. We represent families against nursing homes, assisted living facilities and group homes. Our attorneys have decades of experience holding care providers accountable when residents are harmed. We are committed to every client, offering careful review, honest advice and strong advocacy from the first call until the case is resolved. Contact us today for a free case review.</p>
    <span class="btn btn-olive">Read More</span>
  </section>

  <section class="practice">
    <h2>WELCOME TO OUR FIRM</h2>
    <p>Lorem Ipsum is simply dummy text of the printing and typesetting industry. Lorem Ipsum has been the industry's standard dummy text ever since the 1500s.</p>
    <div class="cards">
      <div class="card">
        <svg class="icon" viewBox="0 0 32 32"><circle cx="16" cy="16" r="16" fill="#fff"/><g fill="#7b7650"><rect x="9" y="9" width="10" height="5" transform="rotate(-40 14 11.5)"/><rect x="14" y="13" width="3" height="10" transform="rotate(-40 15.5 18)"/><rect x="8" y="22" width="12" height="2"/></g></svg>
        <h3>Injured Law</h3>
        <p>Lorem ipsum dolor sit amet consectetur, sed do eiusmod tempor.</p>
        <span class="more">Read More</span>
      </div>
      <div class="card">
        <svg class="icon" viewBox="0 0 32 32"><circle cx="16" cy="16" r="16" fill="#fff"/><text x="16" y="22" text-anchor="middle" font-family="Lato,sans-serif" font-weight="900" font-size="17" fill="#7b7650">$</text></svg>
        <h3>Property Law</h3>
        <p>Lorem ipsum dolor sit amet consectetur, sed do eiusmod tempor.</p>
        <span class="more">Read More</span>
      </div>
      <div class="card">
        <svg class="icon" viewBox="0 0 32 32"><circle cx="16" cy="16" r="16" fill="#fff"/><g fill="#7b7650"><polygon points="8,13 16,8 24,13"/><rect x="10" y="14" width="2" height="8"/><rect x="15" y="14" width="2" height="8"/><rect x="20" y="14" width="2" height="8"/><rect x="8" y="22" width="16" height="2"/></g></svg>
        <h3>Workplace Law</h3>
        <p>Lorem ipsum dolor sit amet consectetur, sed do eiusmod tempor.</p>
        <span class="more">Read More</span>
      </div>
    </div>
  </section>

  <section class="contact">
    <div class="team">
      <div class="team-photo" role="img" aria-label="Legal team meeting around a laptop"></div>
      <p>Our attorneys review every case with care and explain each step clearly.</p>
    </div>
    <form class="ask">
      <h2>ASK US A QUESTION</h2>
      <div class="field">Name</div>
      <div class="field">Email</div>
      <div class="field">Phone</div>
      <div class="field message">Message</div>
      <span class="btn btn-olive">Submit</span>
    </form>
  </section>

  <footer class="footer">
    <div class="col"><h4>Main Menu</h4><ul><li>Home</li><li>About Tarvelin Law Project</li><li>Results</li><li>Our Team</li><li>Resources</li><li>Blog</li><li>Contact Us</li></ul></div>
    <div class="col"><h4>Quick Links</h4><ul><li>Common Rules</li><li>Elder Rights</li><li>Free Case Evaluation</li><li>Testimonials</li><li>Sitemap</li></ul></div>
    <div class="col"><h4>Services</h4><ul><li>Nursing Homes</li><li>Group Homes</li></ul><h4 class="follow">Follow Us On</h4><div class="socials"><span></span><span></span><span></span><span></span></div></div>
    <div class="col news"><h4>Newsletter</h4><ul><li>Sign up for our updates</li></ul><input aria-label="Name"><input aria-label="Email"><span class="btn">Submit</span></div>
  </footer>
  <div class="copyright">Copyright © Tarvelin Law. All Rights Reserved.</div>
</div>
</body>
</html>
```